Business Card and Word .doc header and footer required

I need a business card designed for my cybersecurity consulting company. Also required, is a header and footer to be ued for my word documents.
Attached is the Logo design, font and rgb used.

Industry/Entity Type

Cyber Security Consulting

Contact Information for Business Card

Name, Phone, email, website

Colors
0054AA
0677BA
7BADD7
CADEEF
E8F1F8

Requirements
Must have
• Sleek, modern

```html
<!DOCTYPE html>
<html lang="en">
<head>
<meta charset="utf-8">
<title>Halvard Reach Consulting – Business Card</title>
<link href="https://fonts.googleapis.com/css2?family=Outfit:wght@400;500;600;700&display=swap" rel="stylesheet">
<style>
  :root{
    --backdrop:#06223f;
    --card:#18203b;
    --card-light:#222c4a;
    --brand-blue:#1a7fad;
    --icon-ink:#2e5f80;
    --white:#ffffff;
  }
  *{margin:0;padding:0;box-sizing:border-box}
  html,body{width:1050px;height:1200px;overflow:hidden;background:var(--backdrop)}
  body{position:relative;font-family:'Outfit',sans-serif;color:var(--white)}
  .card{position:absolute;left:105px;width:840px;height:480px;background:var(--card);border-radius:30px;overflow:hidden;box-shadow:0 6px 14px rgba(0,0,0,.25)}
  .card--front{top:81px}
  .card--back{top:639px}

  /* front */
  .hex-pattern{position:absolute;left:0;top:0;width:840px;height:405px;background:linear-gradient(180deg,var(--card-light),var(--card))}
  .lanyard-slot{position:absolute;left:335px;top:0;width:170px;height:31px;background:var(--white)}
  .brand-mark{position:absolute;left:362px;top:106px;width:124px;height:124px;border:12px solid var(--brand-blue);border-radius:50%}
  .brand-name{position:absolute;left:0;top:283px;width:840px;text-align:center;font-weight:700;font-size:39px;letter-spacing:.3px;line-height:1}
  .brand-descriptor{position:absolute;left:0;top:327px;width:840px;display:flex;justify-content:center;align-items:center;gap:5px;font-weight:500;font-size:17px;letter-spacing:5.4px;line-height:1}
  .brand-descriptor::before,.brand-descriptor::after{content:"";width:21px;height:1.5px;background:var(--white)}
  .brand-descriptor::after{margin-left:-5px}
  .web-rule{position:absolute;top:440px;height:4px;background:var(--white)}
  .web-rule--left{left:0;width:297px}
  .web-rule--right{left:542px;width:298px}
  .web-address{position:absolute;left:297px;top:430px;width:245px;text-align:center;font-weight:600;font-size:18px;letter-spacing:3px}

  /* back */
  .network-pattern{position:absolute;left:0;top:0;width:390px;height:480px;background:linear-gradient(90deg,var(--card-light),var(--card))}
  .back-brand{position:absolute;left:176px;top:97px;display:flex;align-items:center;gap:14px}
  .back-brand__mark{width:92px;height:94px;border:9px solid var(--brand-blue);border-radius:50%}
  .back-brand__name{font-weight:700;font-size:24px;letter-spacing:.3px}
  .person{position:absolute;left:179px;top:218px;padding-left:28px;border-left:6px solid var(--white)}
  .person__name{font-weight:700;font-size:40px;line-height:1;letter-spacing:.5px;margin-top:2px}
  .person__role{font-weight:400;font-size:31px;letter-spacing:3.2px;margin-top:6px;line-height:1}
  .divider{position:absolute;left:537px;top:75px;width:2px;height:338px;background:var(--white)}
  .contact{position:absolute;left:565px;display:flex;gap:7px}
  .contact__icon{flex:none;width:39px;height:39px;border-radius:50%;background:var(--white);display:flex;align-items:center;justify-content:center}
  .contact__icon svg{width:22px;height:22px}
  .contact__label{font-weight:600;font-size:15px;line-height:17.5px;letter-spacing:.3px}
  .contact__value{font-weight:400;font-size:15px;line-height:17.5px;letter-spacing:2px}
</style>
</head>
<body>

<section class="card card--front">
  <div class="hex-pattern" role="img" aria-label="Faint hexagonal cube line pattern"></div>
  <div class="lanyard-slot"></div>
  <div class="brand-mark"></div>
  <h1 class="brand-name">HALVARD REACH</h1>
  <div class="brand-descriptor">CONSULTING</div>
  <div class="web-rule web-rule--left"></div>
  <p class="web-address">www.company.com</p>
  <div class="web-rule web-rule--right"></div>
</section>

<section class="card card--back">
  <div class="network-pattern" role="img" aria-label="Faint connected node network pattern"></div>
  <div class="back-brand">
    <div class="back-brand__mark"></div>
    <span class="back-brand__name">HALVARD REACH</span>
  </div>
  <div class="person">
    <h2 class="person__name">JOHN DOE</h2>
    <p class="person__role">General Manager</p>
  </div>
  <div class="divider"></div>

  <div class="contact" style="top:75px">
    <div class="contact__icon"><svg viewBox="0 0 24 24"><path d="M12 2a6.5 6.5 0 0 0-6.5 6.5c0 4.8 6.5 13 6.5 13s6.5-8.2 6.5-13A6.5 6.5 0 0 0 12 2zm0 9.3a2.8 2.8 0 1 1 0-5.6 2.8 2.8 0 0 1 0 5.6z" fill="var(--icon-ink)"/></svg></div>
    <div><p class="contact__label">Visit Us here</p><p class="contact__value">Your address Here<br>Line two here<br>Line three here</p></div>
  </div>
  <div class="contact" style="top:164px">
    <div class="contact__icon"><svg viewBox="0 0 24 24" fill="none" stroke="var(--icon-ink)" stroke-width="1.2"><circle cx="12" cy="12" r="10"/><ellipse cx="12" cy="12" rx="4.5" ry="10"/><path d="M2 12h20M12 2v20M4 7h16M4 17h16"/></svg></div>
    <div><p class="contact__label">Visit Our Website</p><p class="contact__value">www.company.com</p></div>
  </div>
  <div class="contact" style="top:234px">
    <div class="contact__icon"><svg viewBox="0 0 24 24" fill="none" stroke="var(--icon-ink)" stroke-width="1.4"><rect x="3" y="6" width="18" height="13" rx="2"/><path d="M3.5 7l8.5 6.5L20.5 7"/></svg></div>
    <div><p class="contact__label">Email Address</p><p class="contact__value">john@company.com</p></div>
  </div>
  <div class="contact" style="top:304px">
    <div class="contact__icon"><svg viewBox="0 0 24 24"><path d="M6.6 10.8a15.2 15.2 0 0 0 6.6 6.6l2.2-2.2c.3-.3.7-.4 1-.2 1.1.4 2.3.6 3.6.6.6 0 1 .4 1 1V20c0 .6-.4 1-1 1A17 17 0 0 1 3 4c0-.6.4-1 1-1h3.5c.6 0 1 .4 1 1 0 1.3.2 2.5.6 3.6.1.3 0 .7-.2 1z" fill="var(--icon-ink)"/></svg></div>
    <div><p class="contact__label">Office Number</p><p class="contact__value">+009XXXXXXXX</p></div>
  </div>
  <div class="contact" style="top:374px">
    <div class="contact__icon"><svg viewBox="0 0 24 24"><path d="M6.6 10.8a15.2 15.2 0 0 0 6.6 6.6l2.2-2.2c.3-.3.7-.4 1-.2 1.1.4 2.3.6 3.6.6.6 0 1 .4 1 1V20c0 .6-.4 1-1 1A17 17 0 0 1 3 4c0-.6.4-1 1-1h3.5c.6 0 1 .4 1 1 0 1.3.2 2.5.6 3.6.1.3 0 .7-.2 1z" fill="var(--icon-ink)"/></svg></div>
    <div><p class="contact__label">Mobile Number</p><p class="contact__value">+00XXXXXXXXX</p></div>
  </div>
</section>

</body>
</html>
```